Discreet simple classy for adult entertainment

I would like a matte black business card with gold writing for my business. Keeping it simple. Having my following:

Lana frost
Events. Entertainment. Promotions
0491726580

or alternatively could have what i had on my previous card below but i think i prefer the above as again - discretion.

Maybe a nice gold line thru the card or some other very simple design . Or not open to ideas/ can be doublesided if any good ideas with that.

included pics of my old bus card. not sure weather i want a photo on it or not. if i do it wont be the same pic. i kinda wanted a card that was discreet so if it was in someones wallet they wouldn't neccessarily realise it was from a stripper.

Target Market(s)

men

Industry/Entity Type

Business

Contact Information for Business Card

Lana frost
0491726580

Requirements
Nice to have
• i don't know i am really open to anything. im giving my cards to guys so something they can have in their wallet that is discreet preferably.

```html
<!DOCTYPE html>
<html lang="en">
<head>
<meta charset="utf-8">
<title>Lana Frost — Business Card</title>
<link href="https://fonts.googleapis.com/css2?family=Poiret+One&display=swap" rel="stylesheet">
<style>
  :root {
    --card-black: #0b0b0b;
    --card-charcoal: #1c1c1c;
    --gold: #f4b45a;
    --gold-soft: #e9a94d;
  }
  * { margin: 0; padding: 0; box-sizing: border-box; }
  html, body {
    width: 1200px;
    height: 775px;
    overflow: hidden;
    background: var(--card-black);
  }
  .business-card {
    position: relative;
    width: 1200px;
    height: 775px;
    overflow: hidden;
    background:
      radial-gradient(ellipse at 55% 35%, var(--card-charcoal) 0%, rgba(20,20,20,0.6) 35%, transparent 70%),
      radial-gradient(ellipse at 20% 80%, #151515 0%, transparent 55%),
      var(--card-black);
    font-family: "Poiret One", sans-serif;
    color: var(--gold);
    text-align: center;
  }
  .card-name {
    position: absolute;
    top: 105px;
    left: 0;
    width: 100%;
    font-size: 128px;
    font-weight: 400;
    font-variant: small-caps;
    letter-spacing: 2px;
    line-height: 1;
  }
  .card-divider {
    position: absolute;
    top: 278px;
    left: 50%;
    width: 320px;
    height: 12px;
    transform: translateX(-50%);
  }
  .card-tagline {
    position: absolute;
    top: 428px;
    left: 0;
    width: 100%;
    font-size: 62px;
    letter-spacing: 2px;
    line-height: 1;
  }
  .card-phone {
    position: absolute;
    top: 588px;
    left: 0;
    width: 100%;
    font-size: 64px;
    letter-spacing: 3px;
    line-height: 1;
    display: flex;
    justify-content: center;
    align-items: center;
    gap: 22px;
  }
  .card-phone svg { width: 38px; height: 50px; }
</style>
</head>
<body>
  <main class="business-card">
    <h1 class="card-name">Lana Frost</h1>
    <svg class="card-divider" viewBox="0 0 320 12" aria-hidden="true">
      <path d="M0 6 Q160 2 320 6 Q160 10 0 6 Z" fill="var(--gold)"/>
    </svg>
    <p class="card-tagline">Events. Entertainment. Promotions.</p>
    <p class="card-phone">
      <svg viewBox="0 0 24 32" aria-hidden="true">
        <path d="M6 2 L10 2 L11 9 L8 11 Q9 19 14 24 L17 21 L23 24 L22 30 Q10 31 4 18 Q1 9 6 2 Z" fill="var(--gold)"/>
      </svg>
      <span>0491 726580</span>
    </p>
  </main>
</body>
</html>
```